Redesign of an educational Eye website for Medical Students and Healthcare professionals

www.corvantisportal.com is an educational resource, illustrated using high quality 3D animations, for undergraduate medical students and healthcare professionals to learn about the anatomy of the human eye and associated common eye disorders.

The website was originally developed (using a Joomla template) a couple of years ago and we now want to update the brand and design of the site. Example content and animations can be found at https://www.corvantisportal.com/overview or https://www.corvantisportal.com/ocular-anatomy/orbital-anatomy

We would like a new logo and home page design (to include new colour palette, fonts and updated overall design).

The attached PowerPoint contains an example layout of the revised components we want to appear on the new Home page. We plan to have a hero panel at the top of page playing a short video of some of the animations. Similar to how this site works (www.zembri.uk.com).

We want the new site to feel Professional, Modern and Clean and simple.

Target Market(s)

Undergraduate medical students and Healthcare Professionals

Industry/Entity Type

Medical

Logo Text

Corvantis Portal

Number of Pages Required

1 page

Font styles to use
Sans Serif

Colors

Designer to choose colors to be used in the design.

```html
<!DOCTYPE html>
<html lang="en">
<head>
<meta charset="utf-8">
<title>Corvantis Portal – Home</title>
<link rel="stylesheet" href="https://fonts.googleapis.com/css2?family=Open+Sans:wght@400;600;700;800&display=swap">
<style>
:root{
  --ink:#111111;
  --muted:#4a4a4a;
  --white:#ffffff;
  --brand-blue:#5b7fd8;
  --deep-blue:#2f3f8f;
  --indigo:#4a4f8c;
  --indigo-dark:#3f4782;
  --green:#6a9a1f;
  --green-band:#4b7a27;
  --charcoal:#2b2b2b;
  --night:#1c1414;
  --night-deep:#150f0f;
  --hero-dark:#05070d;
}
*{box-sizing:border-box;margin:0;padding:0}
html,body{width:1200px;height:4444px;overflow:hidden}
body{font-family:"Open Sans",Arial,sans-serif;color:var(--ink);background:var(--white);position:relative}
section,header,nav,footer{position:absolute;left:0;width:1200px;overflow:hidden}
.abs{position:absolute}
.ph{position:absolute}

/* top bar */
.topbar{top:0;height:65px;background:var(--white)}
.brand{left:78px;top:12px;display:flex;align-items:center;gap:10px}
.brand-dot{width:14px;height:14px;border-radius:50%;background:var(--brand-blue)}
.brand-name{font-size:28px;font-weight:600;color:var(--brand-blue);letter-spacing:-.5px}
.user{left:758px;top:8px;display:flex;align-items:center;gap:14px}
.avatar{width:48px;height:48px;border-radius:50%;background:radial-gradient(circle at 50% 40%,#c89a80,#5a3a2c);border:2px solid #ddd}
.user-name{font-size:14px;color:var(--muted)}
.signout{left:912px;top:17px;width:75px;height:30px;background:var(--green);color:var(--white);font-size:12px;font-weight:600;display:flex;align-items:center;justify-content:center}
.social{display:flex;gap:8px}
.social span{width:24px;height:24px;border-radius:50%;background:var(--brand-blue);display:block}
.topbar .social{left:1025px;top:20px}

/* nav */
.mainnav{top:65px;height:42px;background:var(--brand-blue)}
.mainnav a{position:absolute;top:12px;color:var(--white);font-size:13px;font-weight:700;text-decoration:none;transform:translateX(-50%)}

/* hero */
.hero{top:107px;height:604px;background:linear-gradient(90deg,var(--hero-dark) 0%,#0a1020 50%,#0b1428 100%)}
.hero-visual{left:620px;top:0;width:580px;height:604px;background:radial-gradient(circle at 62% 45%,#c0283a 0%,#7a1a3a 22%,#2a2f6a 45%,#0a1020 75%)}
.hero-learn{left:89px;top:168px;font-size:38px;font-weight:700;color:var(--white)}
.hero-title{left:89px;top:210px;font-size:58px;font-weight:700;color:#a9d4ff;letter-spacing:-.5px;white-space:nowrap}
.hero-copy{left:89px;top:282px;width:680px;font-size:15px;line-height:29px;color:#e8ecf5}
.btn-solid{left:89px;top:400px;height:38px;padding:0 14px;background:var(--green);color:var(--white);font-size:14px;font-weight:700;display:flex;align-items:center}
.btn-line{left:380px;top:400px;height:38px;padding:0 14px;border:2px solid var(--white);color:var(--white);font-size:14px;font-weight:700;display:flex;align-items:center}

/* shared titles */
.section-title{position:absolute;left:0;width:1200px;text-align:center;font-size:30px;font-weight:800;letter-spacing:.3px}
.tilde{position:absolute;left:585px;width:30px;height:12px}

/* modules */
.modules{top:711px;height:362px;background:var(--white)}
.modules .section-title{top:46px;color:var(--deep-blue)}
.module{position:absolute;width:300px;text-align:center}
.module-icon{width:80px;height:80px;border-radius:50%;background:#7aa82a;margin:0 auto;display:flex;align-items:center;justify-content:center}
.module h3{margin-top:18px;font-size:17px;font-weight:800}
.module p{margin-top:8px;font-size:13px;line-height:17px;color:var(--muted);padding:0 10px}

/* why */
.why{top:1073px;height:903px;background:linear-gradient(180deg,#50558f,#474c8a)}
.why .section-title{top:40px;color:var(--white)}
.why-img{box-shadow:0 6px 16px rgba(0,0,0,.45)}
.why h3{position:absolute;font-size:18px;font-weight:800;color:var(--white)}
.why p{position:absolute;font-size:13px;line-height:19px;color:#e6e8f4}

/* team */
.team{top:1976px;height:714px;background:var(--white)}
.team .section-title{top:44px;color:var(--ink)}
.member{position:absolute;width:237px;text-align:center}
.member-photo{width:237px;height:365px;border:5px solid var(--white);box-shadow:0 2px 10px rgba(0,0,0,.3)}
.member h4{margin-top:18px;font-size:24px;font-weight:800}
.member span{display:block;font-size:16px;color:var(--muted)}

/* testimonials */
.voices{top:2690px;height:466px;background:linear-gradient(180deg,#333,var(--charcoal))}
.voices .section-title{top:40px;color:var(--white);line-height:42px}
.quote-mark{font-size:110px;font-weight:800;color:var(--white);line-height:1}
.voices p{position:absolute;left:207px;top:170px;width:786px;text-align:center;font-size:14px;line-height:25px;color:#eee}
.voice-avatar{left:554px;top:253px;width:88px;height:88px;border-radius:50%;border:4px solid #8fbf3a;background:radial-gradient(circle at 50% 40%,#d2a58a,#6a4a3a)}
.voice-name{top:352px;left:0;width:1200px;text-align:center;font-size:22px;font-weight:700;color:var(--brand-blue)}
.voice-role{top:386px;left:0;width:1200px;text-align:center;font-size:16px;color:var(--white)}

/* trusted */
.trusted{top:3156px;height:406px;background:var(--white)}
.trusted .section-title{top:48px;color:var(--ink)}
.partner-badge{left:100px;top:140px;width:100px;height:120px;border-radius:10px;background:#d9d3c3}
.placeholder-text{position:absolute;top:184px;width:200px;text-align:center;font-size:26px;line-height:32px;color:#555}

/* free trial */
.trial{top:3562px;height:260px;background:linear-gradient(90deg,var(--indigo-dark),#4a5192)}
.trial-photo{left:89px;top:3473px;width:237px;height:349px;z-index:2;background:linear-gradient(180deg,#a06a4a 0%,#e8e8ec 40%,#d6d8de 100%)}
.trial h2{position:absolute;left:350px;top:48px;font-size:25px;font-weight:800;color:var(--white)}
.trial p{position:absolute;left:350px;top:94px;font-size:14px;color:#e6e8f4}
.trial-btn{left:350px;top:148px;width:201px;height:44px;background:var(--white);color:var(--deep-blue);font-size:14px;font-weight:700;display:flex;align-items:center;justify-content:center}

/* charity */
.charity{top:3822px;height:303px;background:linear-gradient(180deg,#4f7e29,var(--green-band))}
.charity-photo{left:785px;top:0;width:282px;height:297px;background:radial-gradient(circle at 50% 55%,#f0c9ad,#c78d6c 60%,#8a5a45)}
.charity h2{position:absolute;left:89px;top:90px;font-size:25px;font-weight:800;color:var(--white)}
.charity p{position:absolute;left:89px;top:134px;width:690px;font-size:14px;line-height:21px;color:#f0f4e8}

/* newsletter + footer */
.newsletter{top:4125px;height:94px;background:var(--night)}
.newsletter h2{position:absolute;left:89px;top:32px;font-size:24px;font-weight:400;color:var(--white)}
.news-input{left:563px;top:32px;width:450px;height:36px;background:var(--white)}
.news-btn{left:1013px;top:32px;width:101px;height:36px;background:var(--brand-blue);color:var(--white);font-size:13px;display:flex;align-items:center;justify-content:center}
.site-footer{top:4219px;height:225px;background:var(--night)}
.foot-col{position:absolute;top:26px}
.foot-col h5{font-size:13px;font-weight:800;color:var(--brand-blue);margin-bottom:6px}
.foot-col li{list-style:none;font-size:13px;line-height:25px;color:var(--white)}
.foot-col.wide li{line-height:32px}
.copyright{left:0;top:175px;width:1200px;height:50px;border-top:1px solid #3a2e2e;background:var(--night-deep)}
.copyright small{position:absolute;left:89px;top:16px;font-size:13px;color:#ddd}
.copyright .social{position:absolute;left:1016px;top:13px}
</style>
</head>
<body>

<header class="topbar">
  <div class="abs brand"><span class="brand-dot"></span><span class="brand-name">Corvantis Portal</span></div>
  <div class="abs user"><div class="avatar" role="img" aria-label="User profile photo"></div><span class="user-name">John Doe</span></div>
  <div class="abs signout">Sign - out</div>
  <div class="abs social"><span></span><span></span><span></span></div>
</header>

<nav class="mainnav">
  <a style="left:338px">HOME</a>
  <a style="left:459px">ABOUT</a>
  <a style="left:595px">CHAPTERS</a>
  <a style="left:723px">FAQ</a>
  <a style="left:847px">CONTACT</a>
</nav>

<section class="hero">
  <div class="ph hero-visual" role="img" aria-label="3D rendering of a human eye with glowing iris"></div>
  <div class="abs hero-learn">Learn</div>
  <div class="abs hero-title">Faster and Smarter</div>
  <p class="abs hero-copy">Lorem ipsum dolor sit amet, consectetuer adipiscing elit, sed diam nonummy nibh euismod tincidunt ut laoreet&nbsp; Lorem ipsum dolor sit amet, consectetuer adipiscing elit, sed diam nonummy nibh euismod tincidunt ut laoreet</p>
  <div class="abs btn-solid">Undergraduates – Learn more</div>
  <div class="abs btn-line">Healthcare Professionals&nbsp; – Learn more</div>
</section>

<section class="modules">
  <h2 class="section-title">TRAINNING MODULES</h2>
  <svg class="tilde" style="top:96px" viewBox="0 0 30 12"><path d="M2 8 Q8 2 15 6 T28 4" fill="none" stroke="#2f3f8f" stroke-width="3"/></svg>
  <div class="module" style="left:96px;top:120px">
    <div class="module-icon"><svg width="40" height="40" viewBox="0 0 40 40" fill="none" stroke="#fff" stroke-width="3"><path d="M10 6v10a8 8 0 0 0 16 0V6"/><path d="M18 24v4a7 7 0 0 0 14 0v-4"/><circle cx="32" cy="20" r="3"/></svg></div>
    <h3>LOREM IPSUM</h3>
    <p>Lorem ipsum dolor sit amet, consectetuer adipiscing elit, sed diam nonummy nibh euismod tincidunt ut laoreet</p>
  </div>
  <div class="module" style="left:448px;top:120px">
    <div class="module-icon"><svg width="42" height="42" viewBox="0 0 42 42" fill="none" stroke="#fff" stroke-width="3"><path d="M3 21 Q21 4 39 21 Q21 38 3 21Z"/><circle cx="21" cy="21" r="6"/></svg></div>
    <h3>LOREM IPSUM</h3>
    <p>Lorem ipsum dolor sit amet, consectetuer adipiscing elit, sed diam nonummy nibh euismod tincidunt ut laoreet</p>
  </div>
  <div class="module" style="left:798px;top:120px">
    <div class="module-icon"><svg width="40" height="40" viewBox="0 0 40 40" fill="none" stroke="#fff" stroke-width="3"><circle cx="20" cy="12" r="6"/><path d="M8 36v-6a12 10 0 0 1 24 0v6"/><path d="M16 26l4 6 4-6"/></svg></div>
    <h3>LOREM IPSUM</h3>
    <p>Lorem ipsum dolor sit amet, consectetuer adipiscing elit, sed diam nonummy nibh euismod tincidunt ut laoreet</p>
  </div>
</section>

<section class="why">
  <h2 class="section-title">WHY CORVANTIS PORTAL</h2>
  <svg class="tilde" style="top:92px" viewBox="0 0 30 12"><path d="M2 8 Q8 2 15 6 T28 4" fill="none" stroke="#fff" stroke-width="3"/></svg>
  <div class="ph why-img" style="left:86px;top:127px;width:501px;height:332px;background:linear-gradient(180deg,#b98478,#d9a898 50%,#a9766a)" role="img" aria-label="Close-up of eyes with labelled eye muscles"></div>
  <h3 style="left:622px;top:123px">Credible</h3>
  <p style="left:622px;top:160px;width:534px">Lorem Ipsum is simply dummy text of the printing and typesetting industry. Lorem Ipsum has been the industry's standard dummy text ever since the 1500s, when an unknown printer took a galley of type and scrambled it to make a type specimen book. It has survived not only five centuries.</p>
  <div class="ph why-img" style="left:607px;top:518px;width:507px;height:332px;background:linear-gradient(90deg,#1b3f8a 0%,#c9a48c 35%,#3aa84a 60%,#f07a1e 85%,#1b3f8a 100%)" role="img" aria-label="Illustration of a face with eye patch and field of vision angles"></div>
  <h3 style="left:400px;top:518px;width:181px;text-align:right">Visual</h3>
  <p style="left:118px;top:556px;width:463px;text-align:right">Lorem Ipsum is simply dummy text of the printing and typesetting industry. Lorem Ipsum has been the industry's standard dummy text ever since the 1500s, when an unknown printer took a galley of type and scrambled it to make a type specimen book. It has survived not only five centuries.</p>
</section>

<section class="team">
  <h2 class="section-title">MEET THE TEAM</h2>
  <svg class="tilde" style="top:94px" viewBox="0 0 30 12"><path d="M2 8 Q8 2 15 6 T28 4" fill="none" stroke="#2f3f8f" stroke-width="3"/></svg>
  <div class="member" style="left:86px;top:222px"><div class="member-photo" style="background:linear-gradient(180deg,#e8e8e8,#bcbcbc)" role="img" aria-label="Portrait of team member John Doe"></div><h4>John Doe</h4><span>Unknown</span></div>
  <div class="member" style="left:350px;top:149px"><div class="member-photo" style="background:linear-gradient(180deg,#f3efcf,#2c3550)" role="img" aria-label="Portrait of team member John Doe in a suit"></div><h4>John Doe</h4><span>Unknown</span></div>
  <div class="member" style="left:613px;top:222px"><div class="member-photo" style="background:linear-gradient(180deg,#e6eef0,#f5f5f5)" role="img" aria-label="Portrait of team member Jane Doe, a doctor"></div><h4>Jane Doe</h4><span>Unknown</span></div>
  <div class="member" style="left:877px;top:163px"><div class="member-photo" style="background:linear-gradient(180deg,#f2f2f2,#2a2a30)" role="img" aria-label="Portrait of team member John Doe in a suit"></div><h4>John Doe</h4><span>Unknown</span></div>
</section>

<section class="voices">
  <h2 class="section-title">WHAT ARE PEOPLE SAYING<br>ABOUT CORVANTIS PORTAL</h2>
  <svg class="tilde" style="top:138px" viewBox="0 0 30 12"><path d="M2 8 Q8 2 15 6 T28 4" fill="none" stroke="#fff" stroke-width="3"/></svg>
  <div class="abs quote-mark" style="left:108px;top:160px">“</div>
  <div class="abs quote-mark" style="left:1030px;top:176px">”</div>
  <p>Has been the industry's standard dummy text ever since the 1500s, when an unknown printer took a galley of type and scrambled it to make a type specimen book. It has survived not only five centuries, but also the leap into electronic typesetting, remaining essentially unchanged. It was popularised in the 1960s with the release of Letraset.</p>
  <div class="abs voice-avatar" role="img" aria-label="Photo of reviewer John Doe"></div>
  <div class="abs voice-name">John Doe</div>
  <div class="abs voice-role">Unknown</div>
</section>

<section class="trusted">
  <h2 class="section-title">TRUSTED ACROSS THE WORLD</h2>
  <svg class="tilde" style="top:100px" viewBox="0 0 30 12"><path d="M2 8 Q8 2 15 6 T28 4" fill="none" stroke="#2f3f8f" stroke-width="3"/></svg>
  <div class="abs partner-badge"></div>
  <div class="placeholder-text" style="left:353px">Image Goes<br>Here</div>
  <div class="placeholder-text" style="left:638px">Image Goes<br>Here</div>
  <div class="placeholder-text" style="left:928px">Image Goes<br>Here</div>
</section>

<section class="trial">
  <h2>WANT TO TRY CORVANTIS PORTAL FOR FREE</h2>
  <p>Lorem Ipsum is simply dummy text of the printing and typesetting industry.</p>
  <div class="abs trial-btn">START FREE TRIAL</div>
</section>
<div class="ph trial-photo" role="img" aria-label="Smiling female doctor in a white coat"></div>

<section class="charity">
  <div class="ph charity-photo" role="img" aria-label="Hands held together in support"></div>
  <h2>WE GIVE 10% OF OUR PROFIT TO CHARITY</h2>
  <p>Lorem Ipsum is simply dummy text of the printing and typesetting industry. Lorem Ipsum has been the industry's standard dummy text ever since the 1500s, when an unknown printer took a galley of type and scrambled it to make a type specimen book. It has survived not only</p>
</section>

<section class="newsletter">
  <h2>SUBSCRIBE TO OUR NEWSLETTER</h2>
  <div class="abs news-input"></div>
  <div class="abs news-btn">Subscribe</div>
</section>

<footer class="site-footer">
  <div class="foot-col" style="left:89px"><h5>PRODUCTS</h5><ul><li>Employee Engagement</li><li>Employee Effectiveness</li><li>Employee Experience</li><li>Plans &amp; Pricing</li></ul></div>
  <div class="foot-col" style="left:388px"><h5>COMPANY</h5><ul><li>Our Story</li><li>Customers</li><li>Careers</li><li>Blog</li></ul></div>
  <div class="foot-col wide" style="left:646px"><h5>RESOURCES</h5><ul><li>Lorem Ipsum is simply dummy</li><li>Lorem Ipsum is simply dummy</li><li>Lorem Ipsum is simply dummy</li><li>Lorem Ipsum is simply dummy</li></ul></div>
  <div class="foot-col" style="left:1019px"><h5>CONTACT US</h5><ul><li>Email Sales</li><li>Email Support</li></ul></div>
  <div class="abs copyright"><small>Copyright © 2018&nbsp; | &nbsp;All Rights Reserved.</small><div class="social"><span></span><span></span><span></span></div></div>
</footer>

</body>
</html>
```